Medical Staffing Pamphlet

We are starting to staff for Medical positions for the first time, we need pamphlets to take to medical facilities to try to gain new business

Need an copy to edit, many errors.

```html
<!DOCTYPE html>
<html lang="en">
<head>
<meta charset="utf-8">
<title>Careway Staffing Medical – Pamphlet Cover</title>
<link rel="stylesheet" href="https://fonts.googleapis.com/css2?family=Exo+2:wght@400;500;600&display=swap">
<style>
  :root {
    --panel-blue: #4f6393;
    --panel-lilac: #7a7fa8;
    --leaf-green: #35744a;
    --leaf-green-deep: #2d5e44;
    --forest-dark: #0d2a14;
    --forest-mid: #1f5a2c;
    --photo-light: #c9ced8;
    --photo-mid: #8a8f98;
    --photo-dark: #3d4147;
    --accent-orange: #f07f1c;
    --ink: #1c1f24;
    --white: #ffffff;
  }
  * { margin: 0; padding: 0; box-sizing: border-box; }
  html, body { width: 1200px; height: 927px; overflow: hidden; background: var(--white); }
  .cover {
    position: relative;
    width: 1200px;
    height: 927px;
    overflow: hidden;
    font-family: "Exo 2", sans-serif;
  }
  .cover__photo {
    position: absolute;
    left: 0; top: 0;
    width: 800px; height: 927px;
    background:
      radial-gradient(ellipse 260px 180px at 590px 620px, #f4f4f2 0%, rgba(244,244,242,0) 100%),
      radial-gradient(ellipse 420px 300px at 330px 430px, #c99a83 0%, rgba(201,154,131,0) 100%),
      linear-gradient(160deg, var(--photo-light) 0%, var(--photo-mid) 45%, var(--photo-dark) 100%);
  }
  .cover__forest {
    position: absolute;
    left: 0; top: 0;
    width: 800px; height: 927px;
  }
  .cover__pitch {
    position: absolute;
    left: 43px; top: 740px;
    color: var(--white);
    font-weight: 500;
    font-size: 22.5px;
    line-height: 29px;
    text-transform: uppercase;
  }
  .contact {
    position: absolute;
    right: 444px; top: 738px;
    text-align: right;
    color: var(--ink);
  }
  .contact__heading {
    color: var(--accent-orange);
    font-weight: 600;
    font-size: 29px;
    line-height: 34px;
    letter-spacing: -0.5px;
    margin-bottom: 4px;
  }
  .contact__line {
    font-size: 17px;
    line-height: 21.5px;
  }
  .contact__web {
    font-size: 17px;
    line-height: 21px;
    margin-top: 22px;
  }
  .panel {
    position: absolute;
    left: 800px; top: 0;
    width: 400px; height: 927px;
  }
  .panel__bands { position: absolute; inset: 0; }
  .brand-square {
    position: absolute;
    left: 109px; top: 201px;
    width: 181px; height: 181px;
    background: var(--white);
  }
  .brand-name {
    position: absolute;
    left: 0; top: 466px;
    width: 400px;
    text-align: center;
    color: var(--white);
    font-weight: 600;
    font-size: 58px;
    line-height: 69px;
    letter-spacing: 0.5px;
  }
  .tagline {
    position: absolute;
    left: 0; top: 738px;
    width: 400px;
    text-align: center;
    color: var(--white);
    font-size: 24px;
    line-height: 33px;
  }
</style>
</head>
<body>
<main class="cover">
  <div class="cover__photo" role="img" aria-label="Photo of a person at a desk writing notes on a paper pad with a yellow pen"></div>

  <svg class="cover__forest" width="800" height="927" viewBox="0 0 800 927" aria-hidden="true">
    <defs>
      <radialGradient id="forestGlow" cx="0.2" cy="0.65" r="0.85">
        <stop offset="0" stop-color="var(--forest-dark)"/>
        <stop offset="0.65" stop-color="#0f3318"/>
        <stop offset="1" stop-color="var(--forest-mid)"/>
      </radialGradient>
    </defs>
    <circle cx="148" cy="857" r="300" fill="url(#forestGlow)"/>
  </svg>

  <p class="cover__pitch">Our medical<br>staffing specialist<br>will provide you<br>quality employees</p>

  <section class="contact">
    <h2 class="contact__heading">CONTACT US</h2>
    <p class="contact__line">2460 N. Maple Creek Rd.</p>
    <p class="contact__line">Fairhaven, Indiana 47000</p>
    <p class="contact__line">555-014-7400</p>
    <p class="contact__web">carewaystaffing.com</p>
  </section>

  <aside class="panel">
    <svg class="panel__bands" width="400" height="927" viewBox="0 0 400 927" aria-hidden="true">
      <rect width="400" height="927" fill="var(--panel-blue)"/>
      <polygon points="0,396 396,0 720,0 0,720" fill="var(--panel-lilac)"/>
      <polygon points="0,841 841,0 1100,0 0,1100" fill="var(--panel-lilac)"/>
      <circle cx="425" cy="-181" r="345" fill="var(--leaf-green)"/>
      <clipPath id="leafClip"><circle cx="425" cy="-181" r="345"/></clipPath>
      <polygon points="0,0 266,0 0,266" fill="var(--leaf-green-deep)" clip-path="url(#leafClip)"/>
    </svg>
    <div class="brand-square" aria-hidden="true"></div>
    <h1 class="brand-name">CAREWAY<br>STAFFING<br>MEDICAL</h1>
    <p class="tagline">Providing<br>high quality<br>healthcare<br>professionals</p>
  </aside>
</main>
</body>
</html>
```